Seeking a beautiful packaging box for Dusk Haven - an essential oil blend (mock up provided!)

My sleep brand - Dusk Haven - is almost ready to go to market. And I need a box! Dusk Haven is a high end essential oils/sleep hygiene brand.

I need a gorgeous, classy box for our 3 sizes of essential oil product we are selling. I have a draft mockup which is to approximate size (attached), but need some help with the finishing touches and layout so it's really polished. I am looking for simple/monochrome designs using black and off white (think Norvel inspo!)

We are selling a 15mL dropper bottle and two roll ons (5ml, 10ml) of the essential oil blend. These are all amber bottles with black top. The box design will be almost identical for each, with very slight variations due to size differences.

The size of the boxes will be
15mL dropper: 30x30x95mm
10ml roller: 19x19x88mm
5ml roller: 18x18x59mm

Target Market(s)

High end/high price point product, shift workers, mums, people suffering stress and insomnia

Industry/Entity Type

Health And Wellness

Font styles to use
Serif
Sans Serif

Colors

Designer to choose only greyscale colors for use in the design.

Requirements
Must have
• I have attached a word document which includes all the necessary text:
- ingredients
- directions
- cautions
- info on essential oils/dusk haven (abbreviated on the smallest box)

Additionally:
- volume
- our website
- instagram logo/duskhavenau name
- made in australia
- recycle symbol
- 12 month open symbol
Nice to have
• I would like the boxes to be monochromatic: white or off white colour, with black logo and writing. I am open to variations on the logo (ie position of writing in relation to the circle/change of font size), but mostly need help with layout, font, direction of text, design of the blank spaces, patterns etc.
Should not have
• Colours

```html
<!DOCTYPE html>
<html lang="en">
<head>
<meta charset="utf-8">
<title>Dusk Haven – Essential Oil Blend Carton Dielines</title>
<link rel="stylesheet" href="https://fonts.googleapis.com/css2?family=Crimson+Pro:wght@400;600&family=Roboto:wght@400;700&display=swap">
<style>
  :root{
    --backdrop:#d7d6dc;
    --paper:#ffffff;
    --ink:#111111;
    --cut:#2b2b2b;
    --serif:"Crimson Pro", Georgia, serif;
    --sans:"Roboto", Arial, sans-serif;
  }
  *{box-sizing:border-box;margin:0;padding:0}
  html,body{width:1200px;height:741px;overflow:hidden;background:var(--backdrop)}
  .sheet{position:relative;width:1200px;height:741px;overflow:hidden;color:var(--ink);font-family:var(--sans)}
  .dieline{position:absolute;left:0;top:0}
  .dieline .cut{fill:var(--paper);stroke:var(--cut);stroke-width:1}
  .dieline .flap-name{font-family:var(--serif);font-weight:400;fill:var(--ink);text-anchor:middle;letter-spacing:.04em;text-transform:uppercase}

  .panel{position:absolute;border:1.3px solid var(--ink);border-radius:3px;background:var(--paper);overflow:hidden}
  .panel > *, .rot > *{position:absolute}
  .rot{left:0;top:0;transform-origin:0 0}

  .brand-name{font-family:var(--serif);font-weight:400;text-transform:uppercase;letter-spacing:.03em;line-height:1;white-space:nowrap}
  .centered{left:0;right:0;text-align:center}

  .bar{background:var(--ink);color:var(--paper);font-family:var(--sans);font-weight:700;text-transform:uppercase;line-height:1;padding:1.5px 3px;white-space:nowrap}
  .tag{background:var(--ink);color:var(--paper);font-family:var(--serif);font-weight:400;text-align:center;line-height:1.15;white-space:nowrap}
  .serif-note{font-family:var(--serif);text-align:center;line-height:1.35}
  .copy{font-family:var(--sans);line-height:1.25;text-align:center}
  .copy p{margin-bottom:.9em}
  .copy h4{font-weight:700;font-size:1em;text-transform:uppercase;margin-top:.8em}
  .copy b{font-weight:700}
  .ingredients{font-family:var(--sans);line-height:1.22;text-align:left}
  .rot-copy{font-family:var(--sans);line-height:1.25;text-align:left}

  .social-square{display:block;border:2.4px solid var(--ink);border-radius:3px;left:50%;transform:translateX(-50%)}
  .handle{font-family:var(--serif);font-weight:600;text-align:center}
  .web{font-family:var(--serif);text-align:center;line-height:1.2}
  .web .url{display:inline-block;background:var(--ink);color:var(--paper);padding:0 2px}
  .symbols{display:flex;justify-content:center;align-items:center;gap:8%}
  .recycle-badge{display:block;border:1.6px solid var(--ink);border-radius:50%}
</style>
</head>
<body>
<main class="sheet">

  <svg class="dieline" width="1200" height="741" viewBox="0 0 1200 741" aria-hidden="true">
    <defs>
      <symbol id="open-jar" viewBox="0 0 40 30">
        <path d="M6 8 L30 2 L31 5 L7 11 Z" fill="none" stroke="#111" stroke-width="1.6"/>
        <path d="M5 14 H35 V25 Q35 28 32 28 H8 Q5 28 5 25 Z" fill="none" stroke="#111" stroke-width="1.8"/>
        <line x1="5" y1="17" x2="35" y2="17" stroke="#111" stroke-width="1.2"/>
        <text x="20" y="26" text-anchor="middle" font-family="Roboto, Arial, sans-serif" font-weight="700" font-size="9" fill="#111">12M</text>
      </symbol>
    </defs>

    <g class="carton carton--15">
      <polygon class="cut" points="29,213 58,201 58,539 29,528"/>
      <polygon class="cut" points="59,201 59,189 71,176 83,132 165,132 165,201"/>
      <polygon class="cut" points="272,201 272,132 353,132 365,176 377,189 380,201"/>
      <polygon class="cut" points="59,539 59,551 71,564 83,609 165,609 165,539"/>
      <polygon class="cut" points="272,539 272,609 353,609 365,564 377,551 380,539"/>
      <path class="cut" d="M165 201 V76 Q165 68 173 68 H264 Q272 68 272 76 V201 Z"/>
      <path class="cut" d="M165 539 V664 Q165 672 173 672 H264 Q272 672 272 664 V539 Z"/>
      <rect class="cut" x="58" y="201" width="429" height="339"/>
      <text class="flap-name" x="219" y="143" font-size="13">Dusk Haven</text>
      <text class="flap-name" x="219" y="599" font-size="13">Dusk Haven</text>
    </g>

    <g class="carton carton--10">
      <polygon class="cut" points="519,213 546,201 546,540 519,528"/>
      <polygon class="cut" points="546,201 546,190 556,180 566,153 620,153 620,201"/>
      <polygon class="cut" points="694,201 694,153 750,153 760,180 768,190 768,201"/>
      <polygon class="cut" points="546,540 546,551 556,561 566,588 620,588 620,540"/>
      <polygon class="cut" points="694,540 694,588 750,588 760,561 768,551 768,540"/>
      <path class="cut" d="M620 201 V115 Q620 109 626 109 H688 Q694 109 694 115 V201 Z"/>
      <path class="cut" d="M620 540 V625 Q620 631 626 631 H688 Q694 631 694 625 V540 Z"/>
      <rect class="cut" x="546" y="201" width="295" height="339"/>
      <text class="flap-name" x="657" y="163" font-size="9.5">Dusk Haven</text>
      <text class="flap-name" x="657" y="577" font-size="9.5">Dusk Haven</text>
    </g>

    <g class="carton carton--5">
      <polygon class="cut" points="873,268 891,257 891,485 873,477"/>
      <polygon class="cut" points="891,257 891,247 898,238 905,212 961,212 961,257"/>
      <polygon class="cut" points="1031,257 1031,212 1080,212 1088,238 1096,247 1100,257"/>
      <polygon class="cut" points="891,485 891,495 898,504 905,528 961,528 961,485"/>
      <polygon class="cut" points="1031,485 1031,528 1080,528 1088,504 1096,495 1100,485"/>
      <path class="cut" d="M961 257 V177 Q961 171 967 171 H1025 Q1031 171 1031 177 V257 Z"/>
      <path class="cut" d="M961 485 V564 Q961 570 967 570 H1025 Q1031 570 1031 564 V485 Z"/>
      <rect class="cut" x="891" y="257" width="280" height="228"/>
      <text class="flap-name" x="996" y="221" font-size="9">Dusk Haven</text>
      <text class="flap-name" x="996" y="521" font-size="9">Dusk Haven</text>
    </g>
  </svg>

  <!-- 15 mL -->
  <section class="panel ingredients-panel" style="left:63px;top:205px;width:99px;height:331px">
    <div class="rot" style="width:329px;height:97px;transform:translateY(329px) rotate(-90deg)">
      <div class="brand-name" style="left:6px;top:5px;font-size:15px;line-height:.95">Dusk<br>Haven</div>
      <div class="bar" style="left:6px;top:41px;width:80px;font-size:6px">Ingredients:</div>
      <p class="ingredients" style="left:6px;top:52px;width:290px;font-size:5.7px">Lavandula Angustifolia (Australian Lavender), Vetiveria Zizanoides (Vetiver) Root Oil, Sweet Vanilla Fragrant Oil, Pelargonium Capitatum (Cape Rose Geranium) Leaf Extract, Juniperus Virginiana (Cedarwood) Wood Oil, Citrus Limon (Australian Lemon) Peel Oil, Origanum Majorana (Marjoram) Leaf Oil, Cananga Odorata (Ylang Ylang) Flower Oil, Anthemis Nobilis (Roman Chamomile) Flower Oil.</p>
    </div>
  </section>

  <section class="panel front" style="left:169px;top:205px;width:99px;height:331px">
    <div class="brand-name centered" style="top:104px;font-size:26px">Dusk<br>Haven</div>
    <div class="tag" style="left:4px;right:4px;top:176px;font-size:9px">Essential Oil Blend</div>
    <p class="serif-note centered" style="top:287px;font-size:9px">Made in Australia<br>15mL</p>
  </section>

  <section class="panel directions-panel" style="left:277px;top:205px;width:98px;height:331px">
    <div class="bar" style="left:3px;right:3px;top:22px;font-size:6.2px">Directions:</div>
    <div class="copy" style="left:3px;right:3px;top:30px;font-size:6px">
      <h4>Diffuse</h4><p>Add 4-6 drops to a diffuser or oilburner at night to create a calm and grounded environment.</p>
      <h4>Bathe</h4><p>Add 2-4 drops to a warm bath to help calm the body and mind.</p>
      <h4>Inhale</h4><p>Place 2 drops in the palms of the hands and inhale directly to ease you into a restful sleep.</p>
      <h4>Massage</h4><p>Dilute 4 drops with a carrier oil (such as jojoba or coconut), and massage into the feet before sleep.</p>
    </div>
    <div class="bar" style="left:3px;right:3px;top:212px;font-size:6.2px">Caution:</div>
    <p class="copy" style="left:3px;right:3px;top:227px;font-size:6px">Possible skin sensitivity. Keep out of reach of children. Not for ingestion or internal use. Avoid contact with eyes, inner ears and sensitive areas.</p>
    <div class="brand-name centered" style="top:294px;font-size:12px">Dusk<br>Haven</div>
  </section>

  <section class="panel info-panel" style="left:384px;top:205px;width:100px;height:331px">
    <div class="copy" style="left:4px;right:4px;top:21px;font-size:6.1px">
      <p>Essential Oils have been used for centuries to help prepare the mind and body for sleep.</p>
      <p>Dusk Haven contain a balanced blend of the most sleep supporting essential oils, renowned for their grounding and calming properties.</p>
      <p><b>Lavender</b> for restfulness<br><b>Vetiver</b> for grounding<br><b>Cedarwood</b> for relaxation<br><b>Marjoram</b> for balance<br><b>Roman Chamomile</b> for comfort</p>
      <p>Add Dusk Haven to your nightly bedtime ritual to help support you in achieving deep and rejuvenating sleep.</p>
    </div>
    <span class="social-square" style="top:187px;width:24px;height:24px"></span>
    <div class="handle centered" style="top:215px;font-size:8px">@duskhavenau</div>
    <p class="web centered" style="top:234px;font-size:7.6px">Visit<br><span class="url">www.duskhaven.com.au</span><br>to learn more</p>
    <div class="symbols centered" style="top:284px;height:28px">
      <svg width="30" height="23" viewBox="0 0 40 30"><use href="#open-jar"/></svg>
      <span class="recycle-badge" style="width:25px;height:25px"></span>
    </div>
  </section>

  <!-- 10 mL -->
  <section class="panel ingredients-panel" style="left:551px;top:205px;width:65px;height:331px">
    <div class="rot" style="width:329px;height:63px;transform:translateY(329px) rotate(-90deg)">
      <div class="brand-name" style="left:5px;top:3px;font-size:10px;line-height:.95">Dusk<br>Haven</div>
      <div class="bar" style="left:5px;top:25px;width:84px;font-size:4.8px">Ingredients:</div>
      <p class="ingredients" style="left:5px;top:34px;width:275px;font-size:4.3px">Lavandula Angustifolia (Australian Lavender), Vetiveria Zizanoides (Vetiver) Root Oil, Sweet Vanilla Fragrant Oil, Pelargonium Capitatum (Cape Rose Geranium) Leaf Extract, Juniperus Virginiana (Cedarwood) Wood Oil, Citrus Limon (Australian Lemon) Peel Oil, Origanum Majorana (Marjoram) Leaf Oil, Cananga Odorata (Ylang Ylang) Flower Oil, Anthemis Nobilis (Roman Chamomile) Flower Oil.</p>
    </div>
  </section>

  <section class="panel front" style="left:624px;top:205px;width:66px;height:331px">
    <div class="brand-name centered" style="top:130px;font-size:17px">Dusk<br>Haven</div>
    <div class="serif-note centered" style="top:182px;font-size:7px">Roll on</div>
    <div class="tag" style="left:3px;right:3px;top:194px;font-size:6.8px">Essential Oil Blend</div>
    <p class="serif-note centered" style="top:283px;font-size:7px">Made in Australia<br>10mL</p>
  </section>

  <section class="panel directions-panel" style="left:697px;top:205px;width:66px;height:331px">
    <div class="rot" style="width:329px;height:64px;transform:translateY(329px) rotate(-90deg)">
      <div class="bar" style="left:66px;top:17px;width:86px;font-size:4.8px">Directions:</div>
      <p class="rot-copy" style="left:66px;top:28px;width:108px;font-size:4.6px">Apply directly onto skin. For sensitive skin, dilute with a carrier oil (such as jojoba or coconut) before application.</p>
      <div class="bar" style="left:184px;top:17px;width:84px;font-size:4.8px">Caution:</div>
      <p class="rot-copy" style="left:184px;top:28px;width:140px;font-size:4.6px">Possible skin sensitivity. Keep out of reach of children. Not for ingestion or internal use. Avoid contact with eyes, inner ears and sensitive areas.</p>
    </div>
    <div class="brand-name centered" style="top:287px;font-size:9px">Dusk<br>Haven</div>
  </section>

  <section class="panel info-panel" style="left:771px;top:205px;width:66px;height:331px">
    <div class="copy" style="left:2px;right:2px;top:30px;font-size:5.1px">
      <p>Essential Oils have been used for centuries to help prepare the mind and body for sleep.</p>
      <p>Dusk Haven contain a balanced blend of the most sleep supporting essential oils, renowned for their grounding and calming properties.</p>
      <p><b>Lavender</b> for restfulness<br><b>Vetiver</b> for grounding<br><b>Cedarwood</b> for relaxation<br><b>Marjoram</b> for balance<br><b>Roman Chamomile</b> for comfort</p>
      <p>Add Dusk Haven to your nightly bedtime ritual to help support you in achieving deep and rejuvenating sleep.</p>
    </div>
    <span class="social-square" style="top:202px;width:16px;height:16px;border-width:2px"></span>
    <div class="handle centered" style="top:222px;font-size:5.6px">@duskhavenau</div>
    <p class="web centered" style="top:242px;font-size:5px">Visit<br><span class="url">www.duskhaven.com.au</span><br>to learn more</p>
    <div class="symbols centered" style="top:283px;height:18px">
      <svg width="21" height="16" viewBox="0 0 40 30"><use href="#open-jar"/></svg>
      <span class="recycle-badge" style="width:17px;height:17px"></span>
    </div>
  </section>

  <!-- 5 mL -->
  <section class="panel ingredients-panel" style="left:894px;top:260px;width:64px;height:223px">
    <div class="rot" style="width:221px;height:62px;transform:translateY(221px) rotate(-90deg)">
      <div class="brand-name" style="left:4px;top:3px;font-size:9.5px;line-height:.95">Dusk<br>Haven</div>
      <div class="bar" style="left:4px;top:23px;width:70px;font-size:4.5px">Ingredients:</div>
      <p class="ingredients" style="left:4px;top:32px;width:210px;font-size:4.1px">Lavandula Angustifolia (Australian Lavender), Vetiveria Zizanoides (Vetiver) Root Oil, Sweet Vanilla Fragrant Oil, Pelargonium Capitatum (Cape Rose Geranium) Leaf Extract, Juniperus Virginiana (Cedarwood) Wood Oil, Citrus Limon (Australian Lemon) Peel Oil, Origanum Majorana (Marjoram) Leaf Oil, Cananga Odorata (Ylang Ylang) Flower Oil, Anthemis Nobilis (Roman Chamomile) Flower Oil.</p>
    </div>
  </section>

  <section class="panel front" style="left:964px;top:260px;width:64px;height:223px">
    <div class="brand-name centered" style="top:72px;font-size:16px">Dusk<br>Haven</div>
    <div class="serif-note centered" style="top:116px;font-size:6.2px">Roll on</div>
    <div class="tag" style="left:3px;right:3px;top:127px;font-size:6.2px">Essential Oil Blend</div>
    <p class="serif-note centered" style="top:198px;font-size:6.6px">Made in Australia<br>5mL</p>
  </section>

  <section class="panel directions-panel" style="left:1034px;top:260px;width:64px;height:223px">
    <div class="rot" style="width:221px;height:62px;transform:translateY(221px) rotate(-90deg)">
      <div class="bar" style="left:37px;top:14px;width:71px;font-size:4.4px">Directions:</div>
      <p class="rot-copy" style="left:37px;top:24px;width:84px;font-size:4.2px">Apply directly onto skin. For sensitive skin, dilute with a carrier oil (such as jojoba or coconut) before application.</p>
      <div class="bar" style="left:137px;top:14px;width:71px;font-size:4.4px">Caution:</div>
      <p class="rot-copy" style="left:137px;top:24px;width:80px;font-size:4.2px">Possible skin sensitivity. Keep out of reach of children. Not for ingestion or internal use. Avoid contact with eyes, inner ears and sensitive areas.</p>
    </div>
    <div class="brand-name centered" style="top:203px;font-size:8.5px">Dusk<br>Haven</div>
  </section>

  <section class="panel info-panel" style="left:1102px;top:260px;width:66px;height:223px">
    <div class="copy" style="left:2px;right:2px;top:6px;font-size:4.3px">
      <p>Essential Oils have been used for centuries to help prepare the mind and body for sleep.</p>
      <p>Dusk Haven contain a balanced blend of the most sleep supporting essential oils, renowned for their grounding and calming properties.</p>
      <p><b>Lavender</b> for restfulness<br><b>Vetiver</b> for grounding<br><b>Cedarwood</b> for relaxation<br><b>Marjoram</b> for balance<br><b>Roman Chamomile</b> for comfort</p>
      <p>Add Dusk Haven to your nightly bedtime ritual to help support you in achieving deep and rejuvenating sleep.</p>
    </div>
    <span class="social-square" style="top:146px;width:15px;height:15px;border-width:2px"></span>
    <div class="handle centered" style="top:164px;font-size:5.4px">@duskhavenau</div>
    <p class="web centered" style="top:177px;font-size:4.6px">Visit<br><span class="url">www.duskhaven.com.au</span><br>to learn more</p>
    <div class="symbols centered" style="top:200px;height:17px">
      <svg width="20" height="15" viewBox="0 0 40 30"><use href="#open-jar"/></svg>
      <span class="recycle-badge" style="width:16px;height:16px"></span>
    </div>
  </section>

</main>
</body>
</html>
```